Let's help people Orlanta with better hearing!

I need a business card for my private practice. I am a Dr. of Audiology and focus on hearing and tinnitus (ringing in the ears) treatment. My practice is named "Orlanta Hearing and Tinnitus Solutions". I want to communicate the idea of improved quality of life utilizing a natural color pallet Love the color turquoise as an accent. Want a professional look, while eye catching. I'm open to nontraditional design aesthetic. Something to get excited about and motivate people to improve their lives!

```html
<!DOCTYPE html>
<html lang="en">
<head>
<meta charset="UTF-8">
<title>Orlanta Hearing &amp; Tinnitus Solutions – Business Card</title>
<link rel="stylesheet" href="https://fonts.googleapis.com/css2?family=Open+Sans:wght@300;400&display=swap">
<style>
  :root {
    --turquoise: #7fd3d0;
    --turquoise-bright: #6fd0cc;
    --charcoal: #231f20;
    --ink: #1e1a1b;
    --muted: #cfd6d6;
    --page: #ffffff;
    --text-font: "Open Sans", Arial, sans-serif;
  }
  * { box-sizing: border-box; margin: 0; padding: 0; }
  html, body {
    width: 1200px;
    height: 900px;
    overflow: hidden;
    background: var(--page);
  }
  .stage {
    width: 1200px;
    height: 900px;
    display: flex;
    align-items: center;
    justify-content: center;
    gap: 60px;
  }
  .card {
    width: 525px;
    height: 300px;
    border-radius: 26px;
    padding: 7px;
    font-family: var(--text-font);
  }
  .card__frame {
    width: 100%;
    height: 100%;
    border-radius: 20px;
    border: 7px solid;
    display: flex;
    flex-direction: column;
    align-items: center;
    justify-content: center;
    text-align: center;
  }

  .practice-name {
    font-weight: 300;
    letter-spacing: 1px;
  }

  /* Front */
  .card--front { background: var(--turquoise); }
  .card--front .card__frame {
    border-color: var(--ink);
    background: var(--turquoise);
  }
  .card--front .practice-name {
    color: var(--ink);
    font-size: 38px;
    line-height: 1.25;
  }

  /* Back */
  .card--back { background: var(--charcoal); }
  .card--back .card__frame {
    border-color: var(--turquoise-bright);
    background: var(--charcoal);
  }
  .card--back .practice-name {
    color: var(--turquoise-bright);
    font-size: 17px;
    line-height: 1.3;
  }

  .contact-person { margin-top: 24px; }
  .contact-person__name {
    color: var(--turquoise-bright);
    font-size: 15px;
    letter-spacing: 1px;
  }
  .contact-person__role {
    color: var(--muted);
    font-size: 10px;
    letter-spacing: .5px;
  }
  .contact-details {
    list-style: none;
    margin-top: 16px;
    color: var(--turquoise-bright);
    font-size: 13px;
    line-height: 1.4;
    letter-spacing: .5px;
  }
</style>
</head>
<body>
  <main class="stage">
    <section class="card card--front" aria-label="Card front">
      <div class="card__frame">
        <p class="practice-name">Orlanta<br>Hearing &amp; Tinnitus Solutions</p>
      </div>
    </section>

    <section class="card card--back" aria-label="Card back">
      <div class="card__frame">
        <p class="practice-name">Orlanta<br>Hearing &amp; Tinnitus Solutions</p>
        <div class="contact-person">
          <p class="contact-person__name">Elin Marsh</p>
          <p class="contact-person__role">Manager</p>
        </div>
        <ul class="contact-details">
          <li>555-014-2738</li>
          <li>info@orlanta-hearing.example</li>
          <li>www.orlanta-hearing.example</li>
        </ul>
      </div>
    </section>
  </main>
</body>
</html>
```